Duel Business card

Want an edgy business card that shows both of our companies on each side of the card, OR both together with a cool design.

*Must be edgy: We have attached our two business logos. We are a bail bond and immigration bond company.

Would like the address on one side only.
Need Phone, cell, website, address, and Name

Company Name 1: Cellgate Release Partners
www.cellgatereleasepartners.example

Company Name 2: Borderline Surety Associates
www.borderlinesuretyassociates.example

These cards will need to be easily changeable so I can modify new employees

Target Market(s)

people in jail, takign imigrants out of jail and from being taken back to there country

Industry/Entity Type

Business

Requirements
Must have
• Include both logos attached

```html
<!DOCTYPE html>
<html lang="en">
<head>
<meta charset="utf-8">
<title>Duel Business Cards</title>
<link rel="stylesheet" href="https://fonts.googleapis.com/css2?family=Cormorant+SC:wght@700&display=swap">
<style>
  :root {
    --bg: #3a3a3c;
    --navy: #1c3966;
    --navy-light: #eef1f5;
    --card: #ffffff;
    --ink: #141414;
    --accent-red: #e8625a;
    --accent-gold: #e5b22c;
  }
  * { box-sizing: border-box; margin: 0; padding: 0; }
  html, body { width: 1200px; height: 900px; overflow: hidden; }
  body {
    background: var(--bg);
    display: flex;
    flex-direction: column;
    align-items: center;
    justify-content: center;
    gap: 48px;
    font-family: "Cormorant SC", "Times New Roman", serif;
    font-weight: 700;
    color: var(--ink);
  }
  .card {
    position: relative;
    width: 660px;
    height: 378px;
    background: var(--card);
    overflow: hidden;
    box-shadow: 0 6px 18px rgba(0,0,0,.35);
  }
  .card__band {
    position: absolute;
    left: 0; top: 0; right: 0;
    height: 168px;
    background:
      radial-gradient(ellipse 60% 120% at 58% 100%, var(--navy-light) 0%, rgba(238,241,245,.85) 35%, rgba(238,241,245,0) 75%),
      linear-gradient(90deg, var(--navy) 0%, #7d8fae 40%, #c7d0dd 60%, var(--navy) 100%);
  }
  .card__rule {
    position: absolute;
    left: 0; right: 0; top: 168px;
    height: 6px;
  }
  .card--borderline .card__rule { background: var(--accent-red); }
  .card--cellgate .card__rule { background: var(--accent-gold); }

  .brand {
    position: absolute;
    top: 52px;
    left: 0; right: 0;
    display: flex;
    align-items: center;
    justify-content: center;
    gap: 14px;
    padding-left: 110px;
  }
  .brand__dot {
    width: 46px; height: 46px;
    border-radius: 50%;
    background: var(--navy);
    flex: none;
  }
  .brand__name {
    font-size: 30px;
    line-height: 1;
    color: var(--navy);
    letter-spacing: .5px;
    max-width: 360px;
  }

  .person {
    position: absolute;
    top: 188px;
    left: 160px;
    font-size: 30px;
    letter-spacing: .5px;
  }
  .phones {
    position: absolute;
    top: 186px;
    right: 42px;
    font-size: 25px;
    line-height: 1.05;
    list-style: none;
  }
  .address {
    position: absolute;
    left: 44px;
    top: 244px;
    font-size: 30px;
    line-height: 1.1;
    font-style: normal;
  }
  .web {
    position: absolute;
    left: 0; right: 0;
    bottom: 28px;
    text-align: center;
    padding-left: 150px;
    font-size: 22px;
    letter-spacing: .5px;
  }
</style>
</head>
<body>

  <article class="card card--borderline">
    <div class="card__band"></div>
    <div class="card__rule"></div>
    <div class="brand">
      <span class="brand__dot"></span>
      <span class="brand__name">Borderline Surety Associates</span>
    </div>
    <p class="person">Daniel Reyes</p>
    <ul class="phones">
      <li>P: 555 014 2290</li>
      <li>C: 555 014 2290</li>
    </ul>
    <address class="address">48 Harbor Lane<br>Millbrook, ST 20418</address>
    <p class="web">www.borderlinesuretyassociates.example</p>
  </article>

  <article class="card card--cellgate">
    <div class="card__band"></div>
    <div class="card__rule"></div>
    <div class="brand">
      <span class="brand__dot"></span>
      <span class="brand__name">Cellgate Release Partners</span>
    </div>
    <p class="person">Daniel Reyes</p>
    <ul class="phones">
      <li>P: 555 014 2290</li>
      <li>C: 555 014 2290</li>
    </ul>
    <address class="address">48 Harbor Lane<br>Millbrook, ST 20418</address>
    <p class="web">www.cellgatereleasepartners.example</p>
  </article>

</body>
</html>
```